Owen Tasker Studios Business Card

Looking for a clear, modern, elegant, sharp business card that conveys a professional yet edgy image to my business as a wedding, portrait, and travel photographer. Would like something that looks vintage yet modern. Need a new business card to grow my business. We are growing the business for Wedding and Event Photography as well as fine art Photography. (Mostly Landscapes)
Updates

I’m looking through designs now but I have a new logo that i want using please.

New logo uploaded please redesign using that

PLEASE ALL DESIGNERS LOOK IN BRIEF FOR NEW LOGO

Target Market(s)

Brides, Grooms, Families with Kids, People looking for Fine Art Photography Artwork

Industry/Entity Type

Photographer

Contact Information for Business Card

Unsure

Font styles to use
Serif

Colors

Designer to choose colors to be used in the design.

Requirements
Must have
• My Website:
• http://taskerlens.examplefolio.net
• Phone:
• 323-481-5206
• Email:
• owentaskerlens@mailbox-example.net
Nice to have
• Would like a sort of shine on the printing finish.
• I like black I think it looks good on a business card.
• Can try working with my logo (png that I've attached)

```html
<!DOCTYPE html>
<html lang="en">
<head>
<meta charset="utf-8">
<title>Owen Tasker Studios Business Card</title>
<link href="https://fonts.googleapis.com/css2?family=Questrial&display=swap" rel="stylesheet">
<style>
  :root {
    --backdrop: #3b3b3c;
    --card: #1d1d1f;
    --foil: #8d8d90;
    --ink-white: #f4f4f4;
    --ink-soft: #d9d9d9;
  }
  * { margin: 0; padding: 0; box-sizing: border-box; }
  html, body {
    width: 799px;
    height: 1200px;
    overflow: hidden;
    background: var(--backdrop);
    font-family: "Questrial", "Century Gothic", sans-serif;
  }
  .canvas {
    position: relative;
    width: 799px;
    height: 1200px;
  }
  .card {
    position: absolute;
    left: 80px;
    width: 640px;
    height: 366px;
    background: var(--card);
    border-radius: 30px;
    box-shadow: 0 10px 30px rgba(0,0,0,0.35);
  }
  .card-front { top: 140px; }
  .card-back { top: 694px; }

  /* Front */
  .front-mark {
    position: absolute;
    left: 50%;
    top: 74px;
    width: 78px;
    height: 78px;
    margin-left: -39px;
    border: 2px solid var(--foil);
  }
  .front-name {
    position: absolute;
    left: 0;
    right: 0;
    top: 170px;
    text-align: center;
    color: var(--foil);
    font-size: 46px;
    letter-spacing: 1px;
    line-height: 1;
    text-transform: uppercase;
  }
  .front-studios {
    position: absolute;
    left: 0;
    right: 0;
    top: 226px;
    text-align: center;
    color: var(--foil);
    font-size: 19px;
    letter-spacing: 16px;
    padding-left: 16px;
    text-transform: uppercase;
  }

  /* Back */
  .back-mark {
    position: absolute;
    left: 64px;
    top: 106px;
    width: 132px;
    height: 132px;
    border: 2px solid var(--ink-white);
  }
  .back-details {
    position: absolute;
    left: 236px;
    top: 134px;
  }
  .back-name {
    color: var(--ink-white);
    font-size: 30px;
    letter-spacing: 0.5px;
    margin-bottom: 16px;
  }
  .contact-list { list-style: none; }
  .contact-item {
    display: flex;
    align-items: center;
    gap: 10px;
    color: var(--ink-soft);
    font-size: 15px;
    line-height: 22px;
  }
  .contact-icon {
    width: 12px;
    height: 12px;
    flex: none;
  }
</style>
</head>
<body>
<main class="canvas">
  <section class="card card-front" aria-label="Card front">
    <div class="front-mark"></div>
    <h1 class="front-name">Owen Tasker</h1>
    <p class="front-studios">Studios</p>
  </section>

  <section class="card card-back" aria-label="Card back">
    <div class="back-mark"></div>
    <div class="back-details">
      <h2 class="back-name">Owen Tasker</h2>
      <ul class="contact-list">
        <li class="contact-item">
          <svg class="contact-icon" viewBox="0 0 12 12" aria-hidden="true">
            <path d="M2 1.5h2l1 2.5-1.3 1a6 6 0 0 0 3.3 3.3l1-1.3 2.5 1v2a1 1 0 0 1-1 1A9.5 9.5 0 0 1 1 2.5a1 1 0 0 1 1-1z" fill="var(--ink-soft)"/>
          </svg>
          <span>323-481-5206</span>
        </li>
        <li class="contact-item">
          <svg class="contact-icon" viewBox="0 0 12 12" aria-hidden="true">
            <rect x="0.5" y="2" width="11" height="8" fill="var(--ink-soft)"/>
            <path d="M0.5 2 6 6.5 11.5 2" fill="none" stroke="var(--card)" stroke-width="1"/>
          </svg>
          <span>owentaskerlens@mailbox-example.net</span>
        </li>
        <li class="contact-item">
          <svg class="contact-icon" viewBox="0 0 12 12" aria-hidden="true">
            <circle cx="6" cy="6" r="5.5" fill="var(--ink-soft)"/>
            <path d="M0.5 6h11M6 0.5c-2.5 3-2.5 8 0 11M6 0.5c2.5 3 2.5 8 0 11" fill="none" stroke="var(--card)" stroke-width="0.8"/>
          </svg>
          <span>www.taskerlens.examplefolio.net</span>
        </li>
      </ul>
    </div>
  </section>
</main>
</body>
</html>
```